Book design for Martial Arts Business

TITLE : The Craft of Dojo Keeping

Subtitle : " Master your business , Master your life

Author Wesley Trandell

I need a book cover design for my new book which is on Martial Arts Busines Success.

Simple and Powerful Black and red in Design
Strong font , thats clear and easy to read
the Tag line of the book is " Build your business, Build your life ( I want this to stand out )

Front cover image with dojo

Back image of myself

space for 2 endorsement and writing about the book

I dont want it to look cheesy or American must have an uk feel too

No money on the book whatsoever

I have attached a design so far for you to see but want variations
Updates

Project Deadline Extended
Reason: Not quite got the look on this we will have to extend this

Need extra days to review

Need extra days to review

Target Market(s)

Martial Arts Business owners

Industry/Entity Type

Business

Colors
000000
ec1f27

Requirements
Must have
• Red and Black in colour
• good font thats not standard .. Impactful and clear
• Images used and any other ideas
Nice to have
• No money in it
Should not have
• Clear and powerful design

```html
<!DOCTYPE html>
<html lang="en">
<head>
<meta charset="utf-8">
<title>The Craft of Dojo Keeping – Book Cover</title>
<link rel="stylesheet" href="https://fonts.googleapis.com/css2?family=Bebas+Neue&family=Tinos:wght@700&display=swap">
<style>
  :root {
    --ink: #000000;
    --signal-red: #ec1f27;
    --spine-red: #b5161c;
    --paper: #ffffff;
    --stage: #e9eaec;
    --dojo-dark: #141414;
    --dojo-mid: #2b2b2b;
  }
  * { margin: 0; padding: 0; box-sizing: border-box; }
  html, body { width: 667px; height: 1200px; overflow: hidden; background: var(--stage); }
  .canvas { position: relative; width: 667px; height: 1200px; }

  .cover-spread {
    position: absolute; left: 58px; top: 18px; width: 551px; height: 410px;
    background: var(--ink); overflow: hidden;
  }

  /* Back cover */
  .back-cover { position: absolute; left: 0; top: 0; width: 267px; height: 410px; }
  .tagline-red {
    font-family: "Tinos", "Times New Roman", serif; font-weight: 700;
    color: var(--signal-red); text-transform: uppercase; white-space: nowrap;
  }
  .tagline-white {
    font-family: "Bebas Neue", "Arial Narrow", sans-serif;
    color: var(--paper); white-space: nowrap; letter-spacing: 0.5px;
  }
  .back-cover .tagline-red { position: absolute; left: 31px; top: 40px; font-size: 16.5px; }
  .back-cover .tagline-white { position: absolute; left: 30px; top: 57px; font-size: 34px; line-height: 1; }
  .blurb {
    position: absolute; left: 30px; top: 103px; width: 226px;
    font-family: "Tinos", "Times New Roman", serif; font-weight: 700;
    font-size: 7px; line-height: 7.9px; color: var(--paper); text-align: justify;
  }
  .author-credit {
    position: absolute; font-family: "Tinos", "Times New Roman", serif; font-weight: 700;
    font-size: 10.5px; color: var(--paper); white-space: nowrap;
  }
  .author-credit .label { color: var(--signal-red); }
  .back-cover .author-credit { left: 78px; top: 367px; }

  /* Spine */
  .spine {
    position: absolute; left: 267px; top: 0; width: 17px; height: 410px;
    background: var(--spine-red);
  }
  .spine-title {
    position: absolute; left: 50%; top: 112px;
    transform-origin: 0 0; transform: rotate(90deg) translateY(-50%);
    font-family: "Bebas Neue", "Arial Narrow", sans-serif; font-size: 13.5px;
    color: var(--paper); white-space: nowrap; letter-spacing: 0.4px; line-height: 1;
  }

  /* Front cover */
  .front-cover { position: absolute; left: 284px; top: 0; width: 267px; height: 410px; }
  .dojo-image {
    position: absolute; inset: 0;
    background:
      linear-gradient(180deg, rgba(0,0,0,0.55) 0%, rgba(0,0,0,0.15) 45%, rgba(0,0,0,0.6) 100%),
      linear-gradient(180deg, var(--dojo-dark) 0%, var(--dojo-mid) 40%, #222 62%, var(--dojo-dark) 100%);
  }
  .front-title { position: absolute; left: 0; right: 0; top: 122px; text-align: center; color: var(--paper); font-family: "Bebas Neue", "Arial Narrow", sans-serif; line-height: 1; }
  .front-title .title-main { display: block; font-size: 33px; letter-spacing: 0.6px; }
  .front-title .title-sub { display: block; font-size: 23px; letter-spacing: 0.4px; margin-top: 1px; }
  .front-cover .tagline-red { position: absolute; left: 0; right: 0; top: 193px; text-align: center; font-size: 15px; }
  .front-cover .tagline-white { position: absolute; left: 0; right: 0; top: 210px; text-align: center; font-size: 30px; line-height: 1; }
  .front-cover .author-credit { right: 17px; top: 379px; }
</style>
</head>
<body>
<main class="canvas">
  <section class="cover-spread" aria-label="Book cover spread">
    <article class="back-cover">
      <p class="tagline-red">Build your business</p>
      <p class="tagline-white">BUILD YOUR LIFE</p>
      <p class="blurb">The Craft of Dojo Keeping is a practical guide for instructors who want their school to thrive as a business without losing the spirit of the mat. Drawing on decades of teaching and running a busy club, the author shows how discipline, respect and steady effort apply to every part of the dojo, from the first trial class to the hundredth grading. Inside you will learn how to build a clear timetable, welcome new students, keep families engaged and grow a loyal community that lasts for years. Each chapter blends honest stories with simple tools you can use the same week, covering planning, leadership, staff, marketing and the daily habits that keep standards high. This is not a book of quick tricks or shortcuts. It is a calm and grounded approach to building something worth passing on, written for club owners across the country who care about their craft as much as their members. Whether you teach from a church hall or a full time centre, you will find ideas to bring order to your week, confidence to your decisions and purpose to your teaching. You will see how to set fair standards for grading, how to train assistant instructors who share your values, and how to keep records that make each term easier than the last. There is guidance on choosing a venue, shaping a beginners course, running open days and speaking with parents in a way that builds lasting trust. The author also shares the mistakes he made along the way, from overfilled classes to late nights spent on paperwork, and the quiet changes that turned a struggling club into a steady and welcoming home for students of every age. Read it from cover to cover or keep it close to the front desk as a handbook you return to whenever a new season begins. Build your business and you will find the freedom to build your life, on the mat and beyond it, with the same focus you ask of every student who bows in at the door.</p>
      <p class="author-credit"><span class="label">Author</span> Wesley Trandell</p>
    </article>

    <div class="spine">
      <span class="spine-title">THE CRAFT OF DOJO KEEPING</span>
    </div>

    <article class="front-cover">
      <div class="dojo-image" role="img" aria-label="Dim photograph of an empty dojo interior with wooden floor and wall scrolls"></div>
      <h1 class="front-title">
        <span class="title-main">THE CRAFT</span>
        <span class="title-sub">OF DOJO KEEPING</span>
      </h1>
      <p class="tagline-red">Build your business</p>
      <p class="tagline-white">BUILD YOUR LIFE</p>
      <p class="author-credit"><span class="label">Author</span> Wesley Trandell</p>
    </article>
  </section>
</main>
</body>
</html>
```